TRV Medicaid and Estate Planning

Improve look and feel of existing content. Create consistency between website and brochure aesthetics/theme.

The average monthly cost for a nursing home is about $5,000. Most people cannot afford that. As a result, roughly 65% of all nursing home residents turn to Medicaid to finance their medical care. Medicaid is a state and federally funded Title 19 benefit program, and most people recognize Medicaid as a program to help poor people. But, fewer people recognize Medicaid as a program that can help most middle class families to preserve their wealth and even pass an inheritance—all the while receiving Medicaid benefits to cover the costs of long term care.

Miles T. Corbett
Texas
mcorbett@trvlawgroup.example
(555) 402-7318 x204
Due to a lack of understanding or possibly a stigmatization of “receiving benefits,” a lot of families pay the nursing home from their life savings. But $60,000 a year as a private pay patient will quickly expend most people’s life savings. The next step is usually to sell the family home to continue paying privately. The hard truth is none of that is necessary with proper Medicaid planning. An unfortunate reality is that a great number of families who could have benefitted from Medicaid planning will eventually end up turning to Medicaid when they have exhausted all other resources.

But wouldn’t it be nice to pass an inheritance to the grandchildren? Or, to provide for a special needs child? What about preserving the life savings entirely? These are some of the things an elder law attorney can help with. The Medicaid qualification criteria and its governing law is complex, but it was written with numerous provisions that allow for the protection of the family.

Seventy percent of those over 65 years old will need some form of long term care in their lifetimes. If you or someone you love is within that 70%, consult with an elder law attorney to see what planning options you may have.

Don’t Go Bankrupt Paying a Nursing Home

If your loved one needs long term care, but you cannot afford the cost of a nursing home, what do you do? People all across Texas are asking themselves this same question. The number one payer source for long term care is Medicaid—not long term care insurance, not Medicare, not life savings. So, the question is: are you eligible for nursing home Medicaid?

For a free legal consultation, contact us at (555) 618-2947 or mcorbett@trvlawgroup.example.

http://www.trvlawgroup.example/estate-planning/medicaid-nursing-homes-and-estate-planning/

Target Market(s)

Texas, Colorado, Elder Law and Estate Planning interests

Font styles to use
Serif

Requirements
Must have
• content I submitted

```html
<!DOCTYPE html>
<html lang="en">
<head>
<meta charset="utf-8">
<title>TRV Medicaid and Estate Planning – Tri-fold Brochure</title>
<link rel="stylesheet" href="https://fonts.googleapis.com/css2?family=Libre+Baskerville:wght@400;700&family=Open+Sans:ital,wght@0,400;0,600;0,700;1,400;1,600;1,700&display=swap">
<style>
:root{
  --navy:#1f2a5e;
  --navy-deep:#18214c;
  --orange:#e2691f;
  --gold:#f2b21e;
  --olive:#2f3b1e;
  --tan:#cdbd8c;
  --blue:#2a6fc0;
  --ink:#2b2b2b;
  --paper:#ffffff;
  --stage:#8f8f8f;
  --serif:'Libre Baskerville', Georgia, serif;
  --sans:'Open Sans', Arial, sans-serif;
}
*{box-sizing:border-box;margin:0;padding:0}
html,body{width:1193px;height:1200px;overflow:hidden;background:var(--stage)}
body{font-family:var(--sans);color:var(--ink);position:relative}

.spread{position:absolute;left:216px;width:760px;height:584px;display:flex;background:var(--paper);box-shadow:0 4px 14px rgba(0,0,0,.3)}
.spread--outside{top:10px}
.spread--inside{top:606px}
.panel{position:relative;width:253.33px;height:100%;overflow:hidden;display:flex;flex-direction:column}
.panel + .panel{border-left:1px solid #e6e6e6}

.stripe{display:flex;height:5px;width:100%}
.stripe span{flex:1}
.stripe .s-orange{background:var(--orange);flex:1.4}
.stripe .s-olive{background:var(--olive);flex:.9}
.stripe .s-tan{background:var(--tan);flex:1.2}
.stripe .s-navy{background:var(--navy);flex:1.4}
.stripe .s-gold{background:var(--gold);flex:1}
.stripe--short{width:62%;margin:0 auto}

.headline{font-family:var(--sans);font-weight:700;color:var(--navy);text-transform:uppercase;font-size:12px;line-height:1.3;padding:8px 16px 10px}
.body{font-size:7.4px;line-height:1.45;padding:0 16px}
.body p{margin-bottom:7px}
.center{text-align:center}

.photo{background:linear-gradient(135deg,#d7c4ae,#b8a38c 45%,#efe9e2);margin:0 0 10px}
.photo--seniors{height:148px;margin:0 12px 12px}

.phone-band{background:var(--navy);color:var(--gold);font-weight:700;font-style:italic;font-size:15px;letter-spacing:.3px;padding:10px 14px}
.contact{display:flex;justify-content:space-between;gap:6px;font-size:6.6px;line-height:1.35;padding:7px 12px;color:#333}
.contact b{font-weight:600}
.push{margin-top:auto}

.logo{display:flex;align-items:center;justify-content:center;gap:7px;padding:14px 0 4px}
.logo__mark{width:12px;height:12px;background:var(--orange)}
.logo__name{font-family:var(--serif);font-weight:700;font-size:40px;color:#3a3a3a;letter-spacing:1px;line-height:1}
.logo__firm{font-family:var(--serif);font-size:6.5px;text-transform:uppercase;letter-spacing:.8px;text-align:center;color:#444;padding-bottom:8px}

.cheat{margin:0 14px;border:1px solid var(--gold);padding:8px 10px}
.cheat h3{font-family:var(--sans);font-weight:700;color:var(--navy);font-size:11px;text-align:center;margin-bottom:6px}
.cheat table{width:100%;border-collapse:collapse;font-size:7px}
.cheat td{padding:1.5px 0}
.cheat td:last-child{text-align:right;font-weight:600}

.cover-art{height:160px;background:linear-gradient(160deg,#f2f4f7 0%,#9dbce3 40%,#3e78c4 70%,#2a5ea8 100%)}
.specialties{background:var(--orange);color:#fff;font-size:9.5px;text-transform:uppercase;text-align:center;line-height:1.35;padding:7px 10px;letter-spacing:.3px}
.lead{font-size:7.6px;line-height:1.45;text-align:center;padding:10px 18px}
.lead .name{color:var(--orange)}

.myths{background:var(--navy);color:#fff}
.myths__head{background:#fff;display:flex;align-items:center;gap:10px;padding:14px 14px 12px}
.myths__icon{width:42px;height:42px;border-radius:50%;background:radial-gradient(circle at 35% 30%,#7fc4f4,var(--blue) 60%,#17508f)}
.myths__title{font-weight:700;color:var(--blue);font-size:16px;line-height:1.1}
.myths__title small{display:block;font-weight:400;font-size:14px;text-align:right}
.myths .body{font-size:7.1px;padding:10px 16px 0}
.myth{display:flex;gap:6px;margin-bottom:6px}
.myth::before{content:"";flex:none;width:5px;height:5px;background:var(--gold);margin-top:3px}
.myth em{color:var(--gold);display:block}

.hero{position:absolute;left:253.33px;top:0;width:506.67px;height:262px;background:linear-gradient(110deg,#8d7d6e 0%,#d9cfc6 35%,#eae5e0 55%,#a9b5c4 80%,#cfd6de 100%)}
.inside-logo{position:absolute;right:14px;top:10px;display:flex;align-items:center;gap:5px}
.inside-logo .logo__name{font-size:24px}
.inside-logo .logo__mark{width:8px;height:8px}
.panel--under-hero{padding-top:262px}
.sub{font-weight:700;color:var(--navy);font-size:8.4px;margin:8px 0 3px}
ol.req{padding-left:13px;font-size:7.4px;line-height:1.45}
.web-band{background:var(--navy);color:var(--gold);font-weight:700;font-style:italic;font-size:14px;padding:11px 16px}
</style>
</head>
<body>

<!-- Outside of tri-fold -->
<section class="spread spread--outside">
  <!-- Inside flap -->
  <div class="panel">
    <div class="stripe" style="margin-top:16px;width:86%;margin-left:7%"><span class="s-orange"></span><span class="s-olive"></span><span class="s-tan"></span><span class="s-navy"></span></div>
    <h2 class="headline">Attorney Miles T. Corbett has assisted hundreds of families qualify for Medicaid benefits to cover the cost of long term care.</h2>
    <div class="photo photo--seniors" role="img" aria-label="Photo of smiling seniors giving a thumbs up"></div>
    <div class="body">
      <p>Sometimes families do not need the assistance of an elder law attorney. Sometimes nursing facilities can assist residents apply for benefits.</p>
      <p>But, sometimes families have properties out of state, have earnings above the income cap, or have business interests or promissory notes. Sometimes families just want to protect the family nest egg, or to protect the spouse who is not in the nursing home, or to protect against unexpected surprises that may lead to an eligibility denial.</p>
      <p>In these cases, these families need an elder law attorney to protect them. They need attorney Miles T. Corbett. Contact Thornton, Reyes &amp; Vale today.</p>
    </div>
    <div class="push phone-band">(555) 402-7318 x204</div>
    <div class="stripe" style="height:8px"><span class="s-orange"></span><span class="s-olive"></span><span class="s-tan"></span><span class="s-gold"></span><span class="s-navy"></span></div>
  </div>

  <!-- Back panel -->
  <div class="panel">
    <div class="stripe stripe--short" style="margin-top:16px"><span class="s-gold"></span><span class="s-tan"></span><span class="s-navy"></span></div>
    <div class="lead">
      <p style="margin-bottom:7px">If your loved one needs long term care, but you cannot afford the cost of a nursing home, what do you do? People all across Texas are asking themselves this same question.</p>
      <p style="margin-bottom:7px">The number one payer source for long term care is Medicaid—not long term care insurance, not Medicare, not life savings.</p>
      <p>So, the question is: are you eligible for nursing home Medicaid? Find out with a free legal consultation.</p>
    </div>
    <div class="logo"><span class="logo__mark"></span><span class="logo__name">TRV</span></div>
    <div class="logo__firm">Thornton, Reyes &amp; Vale</div>
    <div class="cheat">
      <h3>Quick Reference Cheat Sheet</h3>
      <table>
        <tr><td>Monthly Income Cap (single)</td><td>$2,205</td></tr>
        <tr><td>Monthly Income Cap (2 spouses in care)</td><td>$4,410</td></tr>
        <tr><td>Countable Asset Cap (single)</td><td>$2,000</td></tr>
        <tr><td>Countable Asset Cap (2 spouses in care)</td><td>$3,000</td></tr>
        <tr><td>Spousal Protected Resource Amount, Min.</td><td>$24,180</td></tr>
        <tr><td>Spousal Protected Resource Amount, Max.</td><td>$120,900</td></tr>
        <tr><td>Minimum Maintenance Needs Allowance</td><td>$3022.50</td></tr>
        <tr><td>Transfer Penalty Divisor</td><td>$162.41</td></tr>
      </table>
    </div>
    <div class="push phone-band">(555) 402-7318 x204</div>
    <div class="contact">
      <div>Visit us on the web at<br><b>www.trvlawgroup.example</b><br>email: mcorbett@trvlawgroup.example</div>
      <div>Riverside Office Park<br>882 Marlow Ave., Suite 310<br>Houston, TX 77002</div>
    </div>
    <div class="stripe" style="height:8px"><span class="s-orange"></span><span class="s-olive"></span><span class="s-tan"></span><span class="s-gold"></span><span class="s-navy"></span></div>
  </div>

  <!-- Front cover -->
  <div class="panel">
    <div class="logo" style="padding-top:18px"><span class="logo__mark"></span><span class="logo__name">TRV</span></div>
    <div class="logo__firm">Thornton, Reyes &amp; Vale</div>
    <div class="cover-art" role="img" aria-label="Illustration of a stethoscope resting on a blue map of the southern United States"></div>
    <div class="specialties">Mineral. Intellectual. Residential.<br>Commercial. Property</div>
    <div class="lead">Don't know how to pay for long term care? For starters, don't pay more than you need to for legal advice. Call to make an appointment with <span class="name">Miles T. Corbett</span> at TRV today.</div>
    <div class="stripe stripe--short"><span class="s-orange"></span><span class="s-olive"></span><span class="s-tan"></span><span class="s-navy"></span></div>
    <div class="lead">Call for an appointment at our Midtown address. We will also meet you on your terms, whether at a nursing facility or a place of your choosing.</div>
    <div class="push phone-band">(555) 402-7318 x204</div>
    <div class="contact">
      <div>Visit us on the web at<br><b>www.trvlawgroup.example</b><br>email: mcorbett@trvlawgroup.example</div>
      <div>Riverside Office Park<br>882 Marlow Ave., Suite 310<br>Houston, TX 77002</div>
    </div>
    <div class="stripe" style="height:8px"><span class="s-orange"></span><span class="s-olive"></span><span class="s-tan"></span><span class="s-gold"></span><span class="s-navy"></span></div>
  </div>
</section>

<!-- Inside of tri-fold -->
<section class="spread spread--inside">
  <div class="panel myths">
    <div class="myths__head">
      <div class="myths__icon" role="img" aria-label="Blue medical emblem"></div>
      <div class="myths__title">Medicaid Myths<small>get the facts!</small></div>
    </div>
    <div class="stripe"><span class="s-orange"></span><span class="s-olive"></span><span class="s-tan"></span><span class="s-gold"></span></div>
    <div class="body">
      <p>Most people know someone who has qualified for Medicaid, so there are a ton of myths out there about what is required to qualify. You wouldn't take medical advice from a plumber, so don't take legal advice from non-lawyers. Below are some of the common myths we hear.</p>
      <div class="myth"><div><em>You earn too much money to be on Medicaid.</em>Myth! If gross monthly earnings are above the $2,205 income cap, you need a Qualified Income Trust.</div></div>
      <div class="myth"><div><em>Medicaid is a program for poor people.</em>Wrong! Most middle class families can benefit from planning for Medicaid.</div></div>
      <div class="myth"><div><em>The state will take your home if you die on Medicaid.</em>Not Completely True! Texas will not take your home automatically, and if you plan properly, Texas probably never will. If you do not plan, though, the house is likely at risk.</div></div>
      <div class="myth"><div><em>You need to give all your stuff away so that you're so broke, you qualify for Medicaid.</em>This is possibly the worst thing you can do! Making uncompensated transfers will cause penalties that may even prevent eligibility.</div></div>
      <div class="myth"><div><em>You cannot leave your descendants an inheritance if you're on Medicaid.</em>Still Wrong! Medicaid recipients who plan properly can and usually do pass on an inheritance.</div></div>
      <div class="myth"><div><em>You should sell your house, cash out life insurance, and liquidate every one of your assets.</em>Please Don't! You may not have to. Talk with an elder law attorney. You might be eligible for Medicaid right now and not even know it.</div></div>
    </div>
  </div>

  <div class="hero" role="img" aria-label="Photo of a smiling caregiver and an elderly woman giving a thumbs up">
    <div class="inside-logo"><span class="logo__mark"></span><span class="logo__name">TRV</span></div>
  </div>

  <div class="panel panel--under-hero">
    <div class="stripe" style="width:90%;margin-left:5%"><span class="s-orange"></span><span class="s-olive"></span><span class="s-tan"></span><span class="s-navy"></span></div>
    <h2 class="headline" style="font-size:10px;padding:8px 16px 4px">What is Medicaid Planning?</h2>
    <div class="body">
      <p>Medicaid Planning usually involves restructuring assets to meet federal and state law eligibility criteria so that your loved one can get the medical care he or she needs and deserves.</p>
      <h3 class="sub">How Do You Qualify for Medicaid?</h3>
      <p>Generally speaking, only seven qualification rules exist. A Nursing Home Medicaid Applicant must:</p>
      <ol class="req">
        <li>be a resident of Texas</li>
        <li>be a citizen of the United States</li>
        <li>be at least 65 years old or disabled</li>
        <li>be in a skilled nursing facility for 30 days</li>
        <li>have a medical necessity for long term care</li>
        <li>have less than $2,205 gross monthly income</li>
        <li>have less than $2,000 in countable resources</li>
      </ol>
    </div>
    <div class="push web-band">www.trvlawgroup.example</div>
    <div class="stripe" style="height:8px"><span class="s-orange"></span><span class="s-olive"></span><span class="s-tan"></span><span class="s-gold"></span><span class="s-navy"></span></div>
  </div>

  <div class="panel panel--under-hero">
    <div class="stripe" style="width:90%;margin-left:5%"><span class="s-gold"></span><span class="s-tan"></span><span class="s-navy"></span></div>
    <div class="body" style="padding-top:8px">
      <h3 class="sub" style="margin-top:0">But, these seven rules have lots of exceptions.</h3>
      <p>By knowing each of the exceptions, an elder law attorney can help you develop a Medicaid eligibility plan that will not only lead to Medicaid qualification but will also preserve the value of your loved one's estate.</p>
      <h3 class="sub">Is Anything Different if the Applicant is Married?</h3>
      <p>Absolutely! Medicaid law has many provisions to ensure the healthy spouse of an ailing senior does not impoverish herself trying to afford her spouse's medical care. When an ailing spouse applies for nursing home Medicaid, the healthier spouse still at home is able to take advantage of the income diversion rules. She can also use the protected resource amount rules. And sometimes, she can even expand the protected resource amount if her monthly income is not in excess of the minimum monthly maintenance needs allowance after utilizing the income diversion rules. Confused yet? No worries. Make an appointment today.</p>
    </div>
    <div class="push phone-band">(555) 402-7318 x204</div>
    <div class="stripe" style="height:8px"><span class="s-orange"></span><span class="s-olive"></span><span class="s-tan"></span><span class="s-gold"></span><span class="s-navy"></span></div>
  </div>
</section>

</body>
</html>
```